Keystone Allies Website

My business has been word of mouth over the last 3 years and has grown. Now I need a website for additional marketing as we have new clients asking for a website.

You have already completed my Logo during an earlier project. I have attached the logo.

We do Staff Augmentation and Operation Support.

What is that?
Staff augmentation is an outsourcing strategy that allows companies to fill specific, temporary roles to achieve business objectives. This staffing method complements existing teams with specific talent, enhancing business capabilities or filling gaps left by members on extended leave.

We work alongside the internal recruiting team to assist clients to meet and exceed financial goals.

```html
<!DOCTYPE html>
<html lang="en">
<head>
<meta charset="utf-8">
<title>Keystone Allies</title>
<link href="https://fonts.googleapis.com/css2?family=Poppins:wght@400;500;600;700;800&display=swap" rel="stylesheet">
<style>
:root{
  --navy:#0e4a6b;
  --navy-deep:#0a3650;
  --sky:#2b7aa8;
  --sky-soft:#cfe3ef;
  --ink:#1d2a33;
  --muted:#6c7780;
  --line:#e3e7ea;
  --band:#6f7275;
  --star:#f2a62b;
  --white:#ffffff;
  --page:#ffffff;
}
*{box-sizing:border-box;margin:0;padding:0}
html,body{width:1200px;height:4776px;overflow:hidden;background:var(--page)}
body{font-family:"Poppins",sans-serif;color:var(--ink);position:relative}
section,header,footer{position:absolute;left:0;width:1200px}
.abs{position:absolute}
.eyebrow{font-size:11px;font-weight:500;letter-spacing:2px;color:var(--muted);text-transform:uppercase}
.heading{font-weight:800;color:var(--ink);text-transform:uppercase;line-height:1.15}
.copy{font-size:14px;line-height:1.6;color:var(--muted)}
.btn{display:inline-block;background:var(--navy);color:var(--white);font-size:12px;font-weight:600;padding:13px 24px;text-transform:uppercase;letter-spacing:.5px}

/* header */
.site-header{top:0;height:80px;z-index:5}
.brand{left:90px;top:20px;display:flex;align-items:center;gap:10px;font-weight:700;font-size:20px;color:var(--navy)}
.brand .dot{width:32px;height:32px;border-radius:50%;background:var(--navy)}
.nav{left:420px;top:30px;display:flex;gap:26px;font-size:12px;font-weight:500;color:var(--ink);white-space:nowrap}
.nav .active{color:var(--navy);border-bottom:2px solid var(--navy);padding-bottom:4px}
.nav-cta{left:866px;top:20px;background:#e9edf0;font-size:11px;font-weight:600;padding:12px 18px;color:var(--ink);white-space:nowrap}
.login{left:1050px;top:30px;display:flex;align-items:center;gap:8px;font-size:12px;font-weight:600}
.login span{width:20px;height:20px;border-radius:50%;background:var(--navy)}

/* hero */
.hero{top:0;height:880px}
.hero-photo{position:absolute;inset:0;height:860px;background:linear-gradient(120deg,#dfe3e6 0%,#bfc7cd 35%,#8f8478 65%,#5c5650 100%)}
.hero-title{left:140px;top:340px;font-size:82px;font-weight:800;color:var(--white);line-height:1.02;letter-spacing:2px}
.hero-btn{left:220px;top:590px}
.hero-next{left:1020px;top:405px;width:56px;height:56px;border-radius:50%;background:var(--white)}

/* recruitment */
.recruit{top:920px;height:460px;text-align:center}
.recruit .eyebrow{position:absolute;left:0;width:100%;top:30px}
.recruit .heading{position:absolute;left:0;width:100%;top:50px;font-size:36px}
.service-item{position:absolute;width:300px}
.service-item h3{font-size:14px;font-weight:700;margin-bottom:6px}
.service-item p{font-size:12px;line-height:1.5;color:var(--muted)}
.service-item.left{text-align:left}
.service-item .ico{position:absolute;top:2px}
.hub{left:515px;top:140px;width:170px;height:230px;display:flex;flex-direction:column;align-items:center;justify-content:center;gap:12px}
.hub .ring{width:150px;height:150px;border-radius:50%;border:14px solid var(--navy)}
.hub .name{font-size:14px;font-weight:700;color:var(--navy);text-transform:uppercase;white-space:nowrap}

/* grow */
.grow{top:1432px;height:600px}
.grow-photo{left:0;top:0;width:600px;height:600px;background:linear-gradient(160deg,#eceeef 0%,#cdd2d6 45%,#3c3f45 100%)}
.grow-text{left:720px;top:150px;width:380px}
.grow-text .heading{font-size:36px;margin:10px 0 18px}
.grow-text .copy{margin-bottom:24px}

/* services band */
.solutions{top:2040px;height:620px}
.band{left:0;top:0;width:1200px;height:420px;background:var(--band)}
.solutions .eyebrow{left:0;width:100%;top:110px;text-align:center;color:#d6d8da}
.solutions .heading{left:0;width:100%;top:130px;text-align:center;font-size:36px;color:var(--white)}
.card{position:absolute;top:196px;width:256px;background:var(--white);box-shadow:0 10px 30px rgba(0,0,0,.12)}
.card .photo{height:190px}
.card .body{padding:24px 22px 30px}
.card h3{font-size:14px;font-weight:700;margin-bottom:10px;text-transform:uppercase;white-space:nowrap}
.card p{font-size:12px;line-height:1.6;color:var(--muted)}

/* testimonial */
.reviews{top:2720px;height:420px}
.reviews .eyebrow{left:110px;top:10px}
.reviews .heading{left:110px;top:30px;font-size:36px;width:420px}
.quote{left:110px;top:140px;width:440px;font-size:15px;line-height:1.6;color:var(--muted)}
.stars{left:110px;top:250px;display:flex;gap:4px}
.person{left:110px;top:284px}
.person b{display:block;font-size:14px;color:var(--navy)}
.person span{font-size:12px;color:var(--muted)}
.arrows{left:110px;top:336px;display:flex;gap:14px}
.avatar{position:absolute;border-radius:50%;background:linear-gradient(140deg,#c9a88c,#6d5c52)}
.bubble{top:20px;background:var(--white);box-shadow:0 4px 14px rgba(0,0,0,.1);font-size:11px;padding:7px 14px;border-radius:18px;color:var(--ink);white-space:nowrap}

/* blog */
.blog{top:3180px;height:600px;text-align:center}
.blog .eyebrow{left:0;width:100%;top:10px}
.blog .heading{left:0;width:100%;top:30px;font-size:36px}
.post{position:absolute;top:140px;width:475px;text-align:left;background:var(--white);box-shadow:0 10px 30px rgba(0,0,0,.1)}
.post .photo{height:250px;position:relative}
.post .tag{position:absolute;left:20px;bottom:-12px;background:var(--navy);color:var(--white);font-size:10px;font-weight:600;padding:4px 10px}
.post .body{padding:28px 26px 26px}
.post .meta{font-size:11px;color:var(--muted);margin-bottom:8px}
.post h3{font-size:16px;font-weight:700;margin-bottom:8px}
.post p{font-size:12px;line-height:1.6;color:var(--muted);margin-bottom:12px}
.post .views{font-size:12px;font-weight:600;color:var(--navy);display:flex;align-items:center;gap:6px}

/* partners */
.partners{top:3820px;height:170px}
.badge{position:absolute;top:0;width:150px;height:150px;border-radius:50%;background:#f4f5f6;box-shadow:0 6px 18px rgba(0,0,0,.08)}
.badge i{position:absolute;left:37px;top:57px;width:76px;height:36px;border-radius:6px;background:#d7dbde}

/* footer */
.site-footer{top:4100px;height:676px;overflow:hidden}
.footer-bg{left:0;top:0}
.newsletter{left:0;width:100%;top:212px;text-align:center;font-size:30px;font-weight:800;color:var(--white);letter-spacing:1px}
.subscribe{left:410px;top:272px;width:380px;height:44px;background:var(--white);display:flex;align-items:center;font-size:12px;color:var(--muted);padding-left:18px}
.subscribe .send{position:absolute;right:0;top:0;width:44px;height:44px;background:var(--navy-deep)}
.foot-brand{left:180px;top:420px;display:flex;align-items:center;gap:10px;font-size:20px;font-weight:700;color:var(--white);white-space:nowrap}
.foot-brand .dot{width:32px;height:32px;border-radius:50%;background:var(--white)}
.socials{left:196px;top:476px;display:flex;gap:10px}
.socials span{width:22px;height:22px;border-radius:50%;background:rgba(255,255,255,.85)}
.foot-col{top:370px;color:var(--white)}
.foot-col h4{font-size:13px;font-weight:700;margin-bottom:12px}
.foot-col li{list-style:none;font-size:11px;line-height:2;color:#d6e3eb}
.contact-row{display:flex;gap:8px;font-size:11px;line-height:1.5;color:#d6e3eb;margin-bottom:10px}
.contact-row i{flex:none;width:14px;height:14px;border-radius:50%;background:var(--white);margin-top:2px}
.copyright{left:0;top:640px;width:100%;height:36px;background:var(--navy-deep);font-size:10px;color:#c5d4de;text-align:center;line-height:36px;letter-spacing:.5px}
</style>
</head>
<body>

<header class="site-header">
  <div class="abs brand"><span class="dot"></span>Keystone Allies</div>
  <nav class="abs nav">
    <span class="active">HOME</span><span>ABOUT US</span><span>JOB</span><span>SERVICE</span><span>NEWS</span><span>CONTACT</span>
  </nav>
  <div class="abs nav-cta">FREE CONSULTATION</div>
  <div class="abs login"><span></span>LOGIN</div>
</header>

<section class="hero">
  <div class="hero-photo" role="img" aria-label="Team of colleagues smiling together around a tablet in a bright office"></div>
  <svg class="abs" style="left:0;top:560px" width="1200" height="320" viewBox="0 0 1200 320" aria-hidden="true">
    <path d="M0 150 C 250 330, 650 300, 1200 40 L1200 320 L0 320 Z" fill="#dbe8f0"/>
    <path d="M0 200 C 300 340, 700 310, 1200 90 L1200 320 L0 320 Z" fill="#ffffff"/>
  </svg>
  <h1 class="abs hero-title">KEYSTONE<br>ALLIES</h1>
  <span class="abs btn hero-btn">Get Free Consultation</span>
  <svg class="abs hero-next" viewBox="0 0 56 56" aria-hidden="true"><path d="M24 19 L33 28 L24 37" stroke="#1d2a33" stroke-width="3" fill="none" stroke-linecap="round"/></svg>
</section>

<section class="recruit">
  <p class="eyebrow">What we do</p>
  <h2 class="heading">The Recruitment<br>Solution for you</h2>

  <div class="service-item left" style="left:140px;top:170px;padding-right:70px">
    <h3>JOBS PLACEMENT</h3>
    <p>Matching skilled people with roles<br>that fit your team goals.</p>
    <svg class="ico" style="left:250px" width="44" height="44" viewBox="0 0 44 44" aria-hidden="true"><circle cx="22" cy="14" r="7" fill="none" stroke="#0e4a6b" stroke-width="3"/><path d="M8 40 C8 28 36 28 36 40" fill="none" stroke="#0e4a6b" stroke-width="3"/></svg>
  </div>
  <div class="service-item left" style="left:140px;top:285px;padding-right:70px">
    <h3>JOBS CONSULTING</h3>
    <p>Guidance for every stage of<br>your hiring plan.</p>
    <svg class="ico" style="left:250px" width="44" height="44" viewBox="0 0 44 44" aria-hidden="true"><rect x="6" y="8" width="32" height="22" rx="3" fill="none" stroke="#0e4a6b" stroke-width="3"/><path d="M14 38 H30" stroke="#0e4a6b" stroke-width="3"/></svg>
  </div>
  <div class="service-item left" style="left:745px;top:170px;padding-left:60px">
    <svg class="ico" style="left:0" width="44" height="44" viewBox="0 0 44 44" aria-hidden="true"><rect x="6" y="6" width="32" height="32" rx="3" fill="none" stroke="#0e4a6b" stroke-width="3"/><path d="M13 16 H31 M13 23 H31 M13 30 H24" stroke="#0e4a6b" stroke-width="3"/></svg>
    <h3>DEVELOP &amp; TRAINING</h3>
    <p>Upskilling programs that help<br>new staff grow quickly.</p>
  </div>
  <div class="service-item left" style="left:745px;top:285px;padding-left:60px">
    <svg class="ico" style="left:0" width="44" height="44" viewBox="0 0 44 44" aria-hidden="true"><rect x="8" y="4" width="28" height="36" rx="3" fill="none" stroke="#0e4a6b" stroke-width="3"/><path d="M15 22 L20 27 L30 16" stroke="#0e4a6b" stroke-width="3" fill="none"/></svg>
    <h3>TEST &amp; INTERVIEW</h3>
    <p>Structured screening so you<br>meet only the right people.</p>
  </div>

  <div class="abs hub"><span class="ring"></span><span class="name">Keystone Allies</span></div>
</section>

<section class="grow">
  <div class="abs grow-photo" role="img" aria-label="Three smiling professionals in business attire standing together"></div>
  <div class="abs grow-text">
    <p class="eyebrow">Who we are</p>
    <h2 class="heading">Help company and<br>employee to grow</h2>
    <p class="copy">We provide staff augmentation and operation support, filling specific roles and working alongside your internal recruiting team to help you meet and exceed financial goals.</p>
    <span class="btn">Find out more</span>
  </div>
</section>

<section class="solutions">
  <div class="abs band"></div>
  <p class="abs eyebrow">Our services</p>
  <h2 class="abs heading">Business shaped solutions</h2>
  <article class="card" style="left:208px">
    <div class="photo" role="img" aria-label="Colleagues reviewing charts at a meeting table" style="background:linear-gradient(150deg,#b9a48f,#5f5147)"></div>
    <div class="body"><h3>Market Research</h3><p>Clear insight into talent markets so every hire is well informed.</p></div>
  </article>
  <article class="card" style="left:472px">
    <div class="photo" role="img" aria-label="Consultant presenting to a small team" style="background:linear-gradient(150deg,#d4c3b4,#7a6a60)"></div>
    <div class="body"><h3>Consulting Service</h3><p>Hands-on advice that shapes a stronger and leaner team.</p></div>
  </article>
  <article class="card" style="left:736px">
    <div class="photo" role="img" aria-label="Business group discussing plans around laptops" style="background:linear-gradient(150deg,#c8c2ba,#6c6660)"></div>
    <div class="body"><h3>Investment Manag...</h3><p>Smart staffing budgets that protect growth and returns.</p></div>
  </article>
</section>

<section class="reviews">
  <svg class="abs" style="left:240px;top:-40px" width="90" height="70" viewBox="0 0 90 70" aria-hidden="true"><path d="M10 60 V35 Q10 10 35 8 V20 Q22 22 22 35 H35 V60 Z M52 60 V35 Q52 10 77 8 V20 Q64 22 64 35 H77 V60 Z" fill="#eef1f3"/></svg>
  <p class="abs eyebrow">Customer review</p>
  <h2 class="abs heading">What our client<br>say about us</h2>
  <p class="abs quote">Their team stepped in fast, filled our open roles and supported operations while our staff were on leave. A reliable partner for any growing business.</p>
  <svg class="abs stars" width="110" height="18" viewBox="0 0 110 18" aria-hidden="true">
    <g fill="#f2a62b">
      <path d="M9 1 L11.3 6.5 L17 7 L12.7 10.8 L14 16.5 L9 13.5 L4 16.5 L5.3 10.8 L1 7 L6.7 6.5 Z"/>
      <path transform="translate(20 0)" d="M9 1 L11.3 6.5 L17 7 L12.7 10.8 L14 16.5 L9 13.5 L4 16.5 L5.3 10.8 L1 7 L6.7 6.5 Z"/>
      <path transform="translate(40 0)" d="M9 1 L11.3 6.5 L17 7 L12.7 10.8 L14 16.5 L9 13.5 L4 16.5 L5.3 10.8 L1 7 L6.7 6.5 Z"/>
      <path transform="translate(60 0)" d="M9 1 L11.3 6.5 L17 7 L12.7 10.8 L14 16.5 L9 13.5 L4 16.5 L5.3 10.8 L1 7 L6.7 6.5 Z"/>
    </g>
    <path transform="translate(80 0)" d="M9 1 L11.3 6.5 L17 7 L12.7 10.8 L14 16.5 L9 13.5 L4 16.5 L5.3 10.8 L1 7 L6.7 6.5 Z" fill="#e3e7ea"/>
  </svg>
  <div class="abs person"><b>–DANA WHITFIELD</b><span>Executive Chair, NY</span></div>
  <svg class="abs arrows" width="100" height="16" viewBox="0 0 100 16" aria-hidden="true">
    <path d="M20 8 H2 M8 2 L2 8 L8 14" stroke="#9aa3aa" stroke-width="2" fill="none"/>
    <path d="M40 8 H96 M90 2 L96 8 L90 14" stroke="#1d2a33" stroke-width="2" fill="none"/>
  </svg>

  <div class="avatar" role="img" aria-label="Client portrait" style="left:640px;top:30px;width:90px;height:90px"></div>
  <div class="avatar" role="img" aria-label="Client portrait" style="left:830px;top:10px;width:50px;height:50px"></div>
  <div class="avatar" role="img" aria-label="Client portrait" style="left:720px;top:140px;width:70px;height:70px"></div>
  <div class="avatar" role="img" aria-label="Featured client portrait" style="left:840px;top:80px;width:180px;height:180px;box-shadow:0 0 0 10px #f1f4f6"></div>
  <div class="abs bubble" style="left:905px">Hi, I'm Leo Park</div>
</section>

<section class="blog">
  <p class="abs eyebrow">Latest news</p>
  <h2 class="abs heading">Latest blog article</h2>
  <article class="post" style="left:100px">
    <div class="photo" role="img" aria-label="Coworkers smiling at a laptop in an office" style="background:linear-gradient(140deg,#c4b3a3,#675b52)"><span class="tag">NEWS</span></div>
    <div class="body">
      <p class="meta">BY ADMIN &nbsp;|&nbsp; 22 AUG 2022</p>
      <h3>SOME BLOG HEADING GOES HERE...</h3>
      <p>Short notes on hiring trends, team support and how flexible staffing keeps your projects moving.</p>
      <span class="views"><svg width="16" height="10" viewBox="0 0 16 10" aria-hidden="true"><ellipse cx="8" cy="5" rx="7" ry="4" fill="none" stroke="#0e4a6b" stroke-width="1.5"/><circle cx="8" cy="5" r="2" fill="#0e4a6b"/></svg>152</span>
    </div>
  </article>
  <article class="post" style="left:625px">
    <div class="photo" role="img" aria-label="Colleagues collaborating at a desk with a computer" style="background:linear-gradient(140deg,#d2ccc5,#716a63)"><span class="tag">NEWS</span></div>
    <div class="body">
      <p class="meta">BY ADMIN &nbsp;|&nbsp; 22 AUG 2022</p>
      <h3>SOME BLOG HEADING GOES HERE...</h3>
      <p>Short notes on hiring trends, team support and how flexible staffing keeps your projects moving.</p>
      <span class="views"><svg width="16" height="10" viewBox="0 0 16 10" aria-hidden="true"><ellipse cx="8" cy="5" rx="7" ry="4" fill="none" stroke="#0e4a6b" stroke-width="1.5"/><circle cx="8" cy="5" r="2" fill="#0e4a6b"/></svg>152</span>
    </div>
  </article>
</section>

<section class="partners">
  <div class="badge" style="left:175px"><i></i></div>
  <div class="badge" style="left:365px"><i></i></div>
  <div class="badge" style="left:555px"><i></i></div>
  <div class="badge" style="left:745px"><i></i></div>
  <div class="badge" style="left:935px"><i></i></div>
</section>

<footer class="site-footer">
  <svg class="abs footer-bg" width="1200" height="676" viewBox="0 0 1200 676" aria-hidden="true">
    <path d="M0 120 C 300 20, 700 -10, 1200 60 L1200 676 L0 676 Z" fill="#0e4a6b"/>
  </svg>
  <h2 class="abs newsletter">NEWSLETTER</h2>
  <div class="abs subscribe">Enter your email address
    <svg class="send" viewBox="0 0 44 44" aria-hidden="true"><path d="M14 22 L30 15 L25 30 L22 24 Z" fill="#ffffff"/></svg>
  </div>

  <div class="abs foot-brand"><span class="dot"></span>Keystone Allies</div>
  <div class="abs socials"><span></span><span></span><span></span><span></span></div>

  <div class="abs foot-col" style="left:460px">
    <h4>QUICK LINKS</h4>
    <ul><li>Home</li><li>About Us</li><li>Our Service</li><li>Projects</li><li>Contact Us</li><li>Last Blog</li></ul>
  </div>
  <div class="abs foot-col" style="left:630px">
    <h4>INFORMATION</h4>
    <ul><li>Site Map</li><li>Terms &amp; Condition</li><li>Privacy Policy</li><li>FAQs</li><li>Customer Service</li><li>Disclaimer</li></ul>
  </div>
  <div class="abs foot-col" style="left:800px;width:200px">
    <h4>CONTACT INFO</h4>
    <div class="contact-row"><i></i><span>Email<br>hello@keystoneallies.co</span></div>
    <div class="contact-row"><i></i><span>Phone<br>+1 555 014 2287</span></div>
    <div class="contact-row"><i></i><span>Office address goes here, the<br>city, state and country</span></div>
  </div>

  <p class="abs copyright">© COPYRIGHT 2022 KEYSTONE ALLIES LLC ALL RIGHTS RESERVED</p>
</footer>

</body>
</html>
```